Large online photo magazine needs redesign

We have previously digitised a historical photographic magazine of around 20,000 printed pages and made it available online. The magazine ran up to the early 1970s, and the content is largely black and white photographs of local events, accompanied by short captions.

Although the content is very rich, the design needs to be revisited so that:
* it is visually appealing
* it is responsive (i.e. works in browsers across all manner of devices)
* is faithful to the nature of the content

There are only a few core page types, and the central one is the article page, an example of which can be seen at:
http://tawaleaf.org.nz/gisborne/issue/KMW73_19600714/t1-body-d4.html

Any design submitted should be based on the treatment of an article page such as the above.

Given the large number of pages on our site, we need a design which can be templated to work for any content in the collection, i.e. we cannot hand-craft our templates to match a given page of content, rather a template must work acceptably well for all content.

The current site, although basic in design, has the advantage that it is quite efficient in the amount of data per page request (around 100k - 200k). While not adverse to web fonts, banner imagery etc, we will carefully consider the benefit gained from any such treatment against the amount of extra data that needs to be downloaded to the client's browser.

For the right design, we are able ourselves to adapt it to a CSS layout.

An example of each core page type is as follows (though for this project we only expect a design for a single page, as itemised above):

http://tawaleaf.org.nz/gisborne/index.html
http://tawaleaf.org.nz/gisborne/about.html
http://tawaleaf.org.nz/gisborne/help.html
http://tawaleaf.org.nz/gisborne/initial/index.html
http://tawaleaf.org.nz/gisborne/search/results?type=section&text=smith&cmdSubmit=Go
http://tawaleaf.org.nz/gisborne/advanced-search/index.html
http://tawaleaf.org.nz/gisborne/issue/KMW73_19600714/t1-front-d1.html
http://tawaleaf.org.nz/gisborne/issue/KMW73_19600714/index.html
http://tawaleaf.org.nz/gisborne/issue/KMW73_19600714/fig-KMW73_19600714_005a.html
http://tawaleaf.org.nz/gisborne/issue/KMW73_19600714/KMW73_19600714_012.html
http://tawaleaf.org.nz/gisborne/issue/KMW73_19600714/thumbnails.html

Reason: Extending the deadline by three days as a number of designers have only recently accepted the invitation.

A general browsing audience of all ages, but skewed towards the older generations, and those interested in family / regional history.

The average user will not be particularly web-savy, and the treatment of the content should not detract / distract from the actual content itself.

Events

• * it is visually appealing
The content should be visually appealing to the audience, which can be defined as a general browsing audience of all ages, but skewed towards the middle and older generations.

* it is responsive (the design can be adapted - by us - to work in browsers across all manner of devices)

The magazine covers (http://tawaleaf.org.nz/gisborne/issues/index.html) offer some possible inspiration for treatment of the material.

```html
<!DOCTYPE html>
<html lang="en">
<head>
<meta charset="utf-8">
<title>Kaiwaka Weekly – No 73 July 14, 1960</title>
<link rel="stylesheet" href="https://fonts.googleapis.com/css2?family=Open+Sans:wght@400;700&family=Courier+Prime:wght@400&display=swap">
<style>
  :root {
    --brand: #c8374f;
    --grey-bar: #e2e2e2;
    --crumb: #e0e0e0;
    --ink: #111;
    --paper: #ffffff;
    --newsprint: #f2edd4;
    --rule: #555;
  }
  * { box-sizing: border-box; margin: 0; padding: 0; }
  html, body { width: 1000px; height: 1200px; overflow: hidden; background: var(--paper); }
  body { font-family: "Open Sans", Verdana, sans-serif; color: var(--brand); position: relative; }
  a { color: var(--brand); text-decoration: none; }

  .page { position: absolute; left: 340px; top: 0; width: 320px; }

  .masthead { height: 38px; background: var(--brand); display: flex; align-items: center; justify-content: center; }
  .masthead-name { color: #fff; font-weight: 700; font-size: 21px; letter-spacing: 1px; text-transform: uppercase; }

  .tools { position: relative; height: 70px; }
  .search { position: absolute; left: 6px; top: 16px; width: 191px; height: 37px; border: 3px solid var(--brand); border-radius: 19px; display: flex; align-items: center; padding: 0 12px 0 15px; justify-content: space-between; }
  .search-label { color: var(--brand); font-size: 18px; opacity: .85; }
  .menu-btn { position: absolute; left: 271px; top: 12px; width: 43px; height: 43px; border: 3px solid var(--brand); border-radius: 50%; display: flex; align-items: center; justify-content: center; }

  .util-bar { height: 28px; background: var(--grey-bar); font-size: 14px; display: flex; align-items: center; padding-left: 6px; white-space: nowrap; }
  .util-bar .sep { margin: 0 7px; color: var(--brand); }

  .crumbs { margin: 10px 0 0 4px; display: flex; flex-wrap: wrap; width: 270px; row-gap: 5px; }
  .crumb { background: var(--crumb); font-size: 14px; height: 21px; line-height: 21px; padding: 0 18px 0 16px; margin-right: -4px; clip-path: polygon(0 0, calc(100% - 10px) 0, 100% 50%, calc(100% - 10px) 100%, 0 100%, 10px 50%); }
  .crumb:first-child { clip-path: polygon(0 0, calc(100% - 10px) 0, 100% 50%, calc(100% - 10px) 100%, 0 100%); padding-left: 9px; }

  .issue-title { margin: 27px 20px 0; font-size: 25px; font-weight: 700; text-align: center; padding-bottom: 5px; border-bottom: 1px solid var(--rule); }

  .pager { margin-top: 20px; height: 38px; position: relative; }
  .pager svg { position: absolute; top: 3px; }

  .spread { display: block; margin: 20px 0 0 20px; width: 279px; height: 179px; background: linear-gradient(90deg, #d8cfa6, #efe8c4 48%, #e8e0b8 52%, #cfc597); border: 2px solid #222; }
  .full-link { display: block; text-align: center; margin-top: 14px; font-size: 15px; text-decoration: underline; }

  .clipping { margin: 22px 0 0 35px; width: 250px; height: 280px; background: var(--newsprint); }
  .clipping-photo { height: 201px; background: linear-gradient(180deg, #6a6963 0%, #3a3936 60%, #2b2a28 100%); }
  .clipping-text { padding: 21px 7px 0 9px; font-family: "Courier Prime", "Courier New", monospace; font-size: 6.4px; line-height: 6.5px; color: var(--ink); text-align: justify; }
  .clipping-text u { text-decoration: underline; }

  .caption { margin: 15px 25px 0; text-align: center; font-size: 15px; line-height: 26px; }
  .clipping-2 { display: block; margin: 9px 0 0 35px; width: 250px; height: 200px; background: linear-gradient(180deg, #ece6cb 0%, #9c9a90 60%, #3a3936 100%); }
</style>
</head>
<body>
<div class="page">
  <header class="masthead"><span class="masthead-name">Kaiwaka Weekly</span></header>

  <div class="tools">
    <div class="search">
      <span class="search-label">Search</span>
      <svg width="24" height="24" viewBox="0 0 24 24" aria-hidden="true"><circle cx="10" cy="10" r="7" fill="none" stroke="#111" stroke-width="3"/><line x1="15" y1="15" x2="22" y2="22" stroke="#111" stroke-width="4" stroke-linecap="round"/></svg>
    </div>
    <a class="menu-btn" href="#" aria-label="Menu">
      <svg width="24" height="20" viewBox="0 0 24 20" aria-hidden="true"><g fill="#111"><rect x="0" y="1" width="4" height="4"/><rect x="6" y="1" width="18" height="4"/><rect x="0" y="8" width="4" height="4"/><rect x="6" y="8" width="18" height="4"/><rect x="0" y="15" width="4" height="4"/><rect x="6" y="15" width="18" height="4"/></g></svg>
    </a>
  </div>

  <nav class="util-bar"><a href="http://tawaleaf.org.nz/gisborne/advanced-search/index.html">Advanced search</a><span class="sep">|</span><a href="http://tawaleaf.org.nz/gisborne/help.html">Help</a><span class="sep">|</span><a href="#">Report an error</a></nav>

  <nav class="crumbs">
    <a class="crumb" href="http://tawaleaf.org.nz/gisborne/index.html">Kaiwaka Weekly</a>
    <a class="crumb" href="http://tawaleaf.org.nz/gisborne/issues/index.html">Issues</a>
    <a class="crumb" href="http://tawaleaf.org.nz/gisborne/issue/KMW73_19600714/index.html">KMW73_19600714</a>
  </nav>

  <h1 class="issue-title">No 73 July 14, 1960</h1>

  <nav class="pager">
    <svg style="left:34px" width="24" height="34" viewBox="0 0 24 34" aria-label="Previous"><polyline points="19,3 5,17 19,31" fill="none" stroke="#111" stroke-width="5"/></svg>
    <svg style="left:144px" width="32" height="26" viewBox="0 0 32 26" aria-label="Contents"><g fill="#111"><rect x="0" y="1" width="5" height="5"/><rect x="8" y="1" width="24" height="5"/><rect x="0" y="10" width="5" height="5"/><rect x="8" y="10" width="24" height="5"/><rect x="0" y="19" width="5" height="5"/><rect x="8" y="19" width="24" height="5"/></g></svg>
    <svg style="left:258px" width="24" height="34" viewBox="0 0 24 34" aria-label="Next"><polyline points="5,3 19,17 5,31" fill="none" stroke="#111" stroke-width="5"/></svg>
  </nav>

  <div class="spread" role="img" aria-label="Scanned magazine spread with portrait photographs of engaged couples, three air hostess sisters and a river bridge"></div>
  <a class="full-link" href="#">View full sized image</a>

  <figure class="clipping">
    <div class="clipping-photo" role="img" aria-label="Black and white photograph of three sisters in air hostess uniforms beside an aircraft"></div>
    <figcaption class="clipping-text"><u>Above</u>: This is probably something of a record&mdash;three sisters who are all air hostesses. They are the Hartley sisters.....Annette, Ilsa, and Lenore, daughters of Mr and Mrs R.T.Hartley, Ashmore Road, Gisborne. <u>Right</u>: And this young lady, Doreen Walsh, of Auckland, has made history in another way. She was the first air hostess to make a scheduled flight to Gisborne, on Sunday of last week. Hostess service has been extended by T.A.S. to include Gisborne flights, beginning with the Sunday services.</figcaption>
  </figure>
  <p class="caption">This is probably something of a re-cord--three sisters who are all air hostesses. They are the Hartley sis-ters.....Annette, Ilsa, and Lenore, daughters of Mr and Mrs R. T. Hart-ley, Ashmore Road, Gisborne.</p>

  <div class="clipping-2" role="img" aria-label="Black and white clipping of an air hostess at an aircraft doorway"></div>
</div>
</body>
</html>
```